business card design for a small scale specialty cut flower farm

We need a business card design for Hollowmere Blossom Farm based in Langley, BC, Canada. We produce specialty, high-end cut flowers and sell locally to florists, local shops and markets and the end user through bouquet subscriptions. The final business card design should be memorable and have a timeless or vintage feel. We would prefer a square shape.

Target Market(s)

florists, shops and seasonal markets, local flower lovers

Industry/Entity Type

Floral

Contact Information for Business Card

Maren Tilde Hofstad, Grower
Langley, BC, Canada
website: hollowmereblossomfarm.com
instagram: @hollowmereblossomfarm
Tel: 604.913.2748
facebook: www.facebook.com/hollowmereblooms/

Font styles to use
Serif
Decorative
Script

Requirements
Must have
• soft black background colour on front side, the included logo and catch phrase: Fresh Local Seasonal
Nice to have
• phone number and website address on front of card, included photo 6539 incorporated onto the back, possibly photo 6609 as well.

```html
<!DOCTYPE html>
<html lang="en">
<head>
<meta charset="utf-8">
<title>Hollowmere Blossom Farm – Business Card</title>
<link rel="stylesheet" href="https://fonts.googleapis.com/css2?family=Montserrat:wght@400;500;600;700&display=swap">
<style>
  :root {
    --backdrop: #2a2a2c;
    --card-black: #1f1b1c;
    --card-white: #ffffff;
    --ink: #1c1c1c;
    --ink-soft: #555555;
    --rule: #bdbdbd;
    --blush: #e7a9cf;
    --petal: #f2c1dc;
  }
  * { box-sizing: border-box; margin: 0; padding: 0; }
  html, body {
    width: 1200px; height: 900px; overflow: hidden;
    background: var(--backdrop);
    font-family: "Montserrat", sans-serif;
  }
  .canvas { position: relative; width: 1200px; height: 900px; }
  .card {
    position: absolute; left: 320px; width: 560px; height: 320px;
    box-shadow: 0 14px 30px rgba(0,0,0,.45);
    overflow: hidden;
  }
  /* Front (black) side */
  .card--front { top: 105px; background: var(--card-black); }
  .front__flower {
    position: absolute; left: 200px; top: 60px; width: 160px; height: 150px;
    border-radius: 50%;
    background: radial-gradient(circle at 50% 50%, #e9e27a 0 14%, #f2c1dc 15% 55%, #4f8a47 56% 70%, rgba(31,27,28,0) 71%);
  }
  .front__tagline {
    position: absolute; right: 40px; bottom: 38px;
    color: var(--blush); font-weight: 600; font-size: 14px; letter-spacing: .5px;
    text-transform: uppercase;
  }
  /* Back (white) side */
  .card--back { top: 475px; background: var(--card-white); }
  .back__brand {
    position: absolute; left: 0; top: 0; width: 280px; height: 320px;
    display: flex; flex-direction: column; align-items: center; justify-content: center;
    color: var(--ink); text-align: center;
  }
  .back__brand-dot {
    width: 40px; height: 40px; border-radius: 50%; background: var(--petal); margin-bottom: 14px;
  }
  .back__brand-name {
    font-weight: 500; font-size: 17px; letter-spacing: 3px; line-height: 1.35;
    text-transform: uppercase;
  }
  .back__divider {
    position: absolute; left: 284px; top: 60px; width: 1px; height: 200px;
    background: var(--rule);
  }
  .contact {
    position: absolute; left: 302px; top: 78px; width: 240px; color: var(--ink);
  }
  .contact__name {
    font-weight: 700; font-size: 16px; letter-spacing: .5px; text-transform: uppercase;
    white-space: nowrap;
  }
  .contact__role { font-size: 12px; color: var(--ink-soft); margin-bottom: 8px; }
  .contact__list { list-style: none; }
  .contact__item {
    display: flex; align-items: center; gap: 6px;
    font-size: 11.5px; line-height: 1; margin-bottom: 9px; white-space: nowrap;
  }
  .contact__icon { width: 14px; height: 14px; flex: none; }
  .contact__gap { margin-top: 16px; }
</style>
</head>
<body>
<main class="canvas">
  <section class="card card--front" aria-label="Card front">
    <div class="front__flower" role="img" aria-label="Watercolour wild rose in pink with green leaves"></div>
    <p class="front__tagline">Fresh Local Seasonal</p>
  </section>

  <section class="card card--back" aria-label="Card back">
    <div class="back__brand">
      <span class="back__brand-dot"></span>
      <p class="back__brand-name">Hollowmere<br>Blossom Farm</p>
    </div>
    <div class="back__divider"></div>
    <div class="contact">
      <p class="contact__name">Maren Tilde Hofstad</p>
      <p class="contact__role">Owner</p>
      <ul class="contact__list">
        <li class="contact__item">
          <svg class="contact__icon" viewBox="0 0 16 16" aria-hidden="true">
            <rect x="1" y="1" width="14" height="14" rx="2" fill="none" stroke="#1c1c1c" stroke-width="1.3"/>
            <path d="M5 4.2c-.8.5-.9 1.6-.3 2.9.8 1.8 2.4 3.5 4.2 4.3 1.2.5 2.2.4 2.7-.3l-1.5-1.5-1.2.6c-1-.5-1.9-1.4-2.4-2.4l.6-1.2z" fill="#1c1c1c"/>
          </svg>
          (604) 913-2748
        </li>
        <li class="contact__item">
          <svg class="contact__icon" viewBox="0 0 16 16" aria-hidden="true">
            <g fill="none" stroke="#1c1c1c" stroke-width="1.2">
              <circle cx="8" cy="8" r="6.5"/>
              <ellipse cx="8" cy="8" rx="3" ry="6.5"/>
              <path d="M1.5 8h13M2.5 4.8h11M2.5 11.2h11"/>
            </g>
          </svg>
          www.hollowmereblossomfarm.com
        </li>
        <li class="contact__item contact__gap">
          <svg class="contact__icon" viewBox="0 0 16 16" aria-hidden="true">
            <circle cx="8" cy="8" r="6.8" fill="none" stroke="#1c1c1c" stroke-width="1.2"/>
          </svg>
          @hollowmereblossomfarm
        </li>
        <li class="contact__item">
          <svg class="contact__icon" viewBox="0 0 16 16" aria-hidden="true">
            <circle cx="8" cy="8" r="6.8" fill="none" stroke="#1c1c1c" stroke-width="1.2"/>
          </svg>
          hollowmereblooms
        </li>
      </ul>
    </div>
  </section>
</main>
</body>
</html>
```